CBD online business for pets and pet parents needs a new website

We need a website for my new online business. I have left a job of 25 years to do my passion. Helping Pets Live healthy and happy lives. I would like to provide my story so that our customer will know why I have started this business-To help!We will be providing all natural CBD (Hemp) products, specialty items, memorials as well as some products for pet parents. We would like our landing page to have our mission, be informative and easy to navigate and maybe feature our treats and oils for pets. We will need a page for pet products, a page for pet memorials, a page for pet lover products and a page for pet parent products.

Target Market(s)

millennials, boomers, pet lovers

Coding

Coded - Design and coding required

Number of Pages Required

5+ page

Colors
33b8a4

Requirements
Nice to have
• diagram of hemp oil extract benefits for dogs and people

```html
<!DOCTYPE html>
<html lang="en">
<head>
<meta charset="utf-8">
<title>Tailwell Co. – Natural CBD Oils & Treats for Pets</title>
<link href="https://fonts.googleapis.com/css2?family=Mulish:wght@400;600;700;800&display=swap" rel="stylesheet">
<style>
:root{
  --teal:#33b8a4;
  --teal-deep:#1fa596;
  --teal-soft:#c9efe9;
  --teal-pale:#e4f7f4;
  --navy:#0d3142;
  --orange:#f26a1b;
  --ink:#1d2b36;
  --text:#5d6670;
  --white:#ffffff;
  --star:#f7b500;
}
*{box-sizing:border-box;margin:0;padding:0}
html,body{width:1200px;height:2946px;overflow:hidden}
body{position:relative;font-family:'Mulish',sans-serif;color:var(--text);background:var(--white)}
.abs{position:absolute}
a{color:inherit;text-decoration:none}

/* top bar */
.topbar{left:0;top:0;width:1200px;height:26px;background:var(--teal-deep);color:var(--white);font-size:10px;font-weight:700}
.topbar .phone{left:250px;top:7px}
.topbar .promo{left:0;width:1200px;top:7px;text-align:center;letter-spacing:.3px}
.topbar .account{left:838px;top:7px}
.topbar .cart{left:906px;top:7px}

/* nav */
.nav{left:0;top:26px;width:1200px;height:72px;background:var(--white)}
.brand{display:flex;align-items:center;gap:8px;font-weight:800;color:var(--teal);font-size:21px}
.brand .dot{width:22px;height:22px;border-radius:50%;background:var(--teal)}
.nav .brand{left:250px;top:22px}
.menu{left:492px;top:30px;display:flex;gap:24px;font-size:11px;font-weight:700;color:var(--ink)}
.menu span.drop::after{content:"";display:inline-block;margin-left:4px;border:3px solid transparent;border-top-color:var(--ink);transform:translateY(2px)}

/* hero */
.hero-bg{left:0;top:98px;width:1200px;height:420px;background:linear-gradient(100deg,#1fa596 0%,#33b8a4 45%,#5cc7b6 100%)}
.hero-wave{left:0;top:400px}
.hero h1{left:250px;top:164px;width:300px;color:var(--white);font-size:28px;line-height:31px;font-weight:800}
.hero p{left:250px;top:276px;width:340px;color:var(--white);font-size:11px;line-height:15px;font-weight:600}
.btn{display:inline-block;border-radius:16px;font-size:11px;font-weight:700;color:var(--white);text-align:center;line-height:30px;height:30px}
.btn.dark{background:var(--navy)}
.btn.orange{background:var(--orange)}
.btn.outline{background:var(--white);border:1.5px solid var(--teal);color:var(--teal);line-height:27px}
.hero .b1{left:250px;top:330px;width:116px}
.hero .b2{left:376px;top:330px;width:124px}
.bag{border-radius:6px;background:linear-gradient(180deg,#ffffff 0%,#ffffff 32%,#33b8a4 32%,#33b8a4 44%,#8cc06a 44%,#6e9c52 100%);box-shadow:0 6px 14px rgba(0,0,0,.18)}
.hero .bag1{left:612px;top:170px;width:108px;height:200px}
.hero .bag2{left:722px;top:152px;width:118px;height:222px}
.hero .bag3{left:846px;top:170px;width:108px;height:200px}

/* shop pills */
.pill{height:94px;width:220px;border-radius:47px;background:var(--white);border:3px solid var(--teal);box-shadow:0 6px 18px rgba(0,0,0,.1);display:flex;align-items:center;gap:16px;padding:0 18px}
.pill .face{width:66px;height:66px;border-radius:50%;background:var(--teal-soft)}
.pill small{display:block;color:var(--teal);font-size:13px;font-weight:700}
.pill strong{display:block;color:var(--ink);font-size:24px;font-weight:800;line-height:26px}
.pill.dogs{left:370px;top:432px}
.pill.cats{left:609px;top:432px}

/* mission */
.h2{color:var(--ink);font-size:29px;font-weight:700;text-align:center;width:1200px;left:0;line-height:36px}
.mission-title{top:583px}
.mission-lead{left:250px;top:638px;width:320px;font-size:15.5px;line-height:20px;color:var(--ink)}
.badges{left:250px;top:746px;display:flex;gap:16px}
.badge{width:70px;text-align:center}
.badge .ring{width:70px;height:70px;border-radius:50%;border:2.5px solid var(--teal);display:flex;align-items:center;justify-content:center;margin-bottom:8px}
.badge span{font-size:9.5px;font-weight:700;color:var(--teal);line-height:12px;display:block}
.mission-body{left:609px;top:638px;width:374px;font-size:10.5px;line-height:15.5px}
.mission-body p{margin-bottom:13px}
.mission .more{left:553px;top:922px;width:94px}

/* soft decorative wash behind the benefits */
.deco-wash{left:0;top:860px;width:560px;height:600px;background:radial-gradient(ellipse at 45% 55%,rgba(51,184,164,.2) 0%,rgba(51,184,164,.08) 50%,rgba(255,255,255,0) 72%)}

/* benefits */
.benefits-title{top:1006px;line-height:32px;font-size:27px}
.pets-photo{left:265px;top:1120px;width:255px;height:284px;border-radius:10px;background:linear-gradient(160deg,#e6cc93 0%,#c79a5a 55%,#8a6a46 100%)}
.benefit{display:flex;align-items:center;gap:12px;font-size:14px;color:var(--ink)}
.benefit i{width:26px;height:26px;border-radius:50%;background:var(--teal);display:flex;align-items:center;justify-content:center}
.benefit i::after{content:"";width:9px;height:9px;border-radius:50%;border:2px solid var(--white)}

/* testimonials */
.testi-bg{left:0;top:1473px;width:1200px;height:590px;background:linear-gradient(180deg,#6fd1c2 0%,#58c6b5 60%,#33b8a4 100%)}
.testi-title{top:1593px}
.card{width:222px;height:243px;background:var(--white);border-radius:6px;box-shadow:0 6px 16px rgba(0,0,0,.1);padding:70px 18px 0;font-size:10px;line-height:15px}
.card .avatar{position:absolute;left:62px;top:-42px;width:98px;height:98px;border-radius:50%;border:3px solid var(--teal);background:linear-gradient(160deg,#c9b59e,#6e5a48)}
.card h3{text-align:center;color:var(--ink);font-size:15px;font-weight:700;margin-top:-6px}
.card .stars{text-align:center;color:var(--star);font-size:11px;letter-spacing:1px;margin-bottom:10px}
.card .issues{color:var(--ink);margin-bottom:6px}
.card .issues b{font-weight:800}
.card .read{color:var(--orange);font-weight:700}
.arrow{width:30px;height:30px;border-radius:50%;border:1.5px solid var(--teal);background:var(--white);display:flex;align-items:center;justify-content:center}
.arrow.grey{border-color:#cfd4d7}
.testi-btn{left:535px;top:1972px;width:130px}

/* popular */
.pop-title{top:2124px}
.product{width:164px;text-align:center}
.product .pbag{width:98px;height:186px;margin:0 auto 22px}
.product .name{font-size:12px;color:var(--text)}
.product .price{font-size:17px;color:var(--ink);margin:3px 0 8px}
.product .btn{width:96px;height:28px;line-height:25px;font-size:10.5px}
.product .btn.orange{line-height:28px}
.featured{left:428px;top:2180px;width:164px;height:324px;background:var(--white);box-shadow:0 8px 20px rgba(0,0,0,.12);border-radius:4px}
.sale{left:423px;top:2174px;width:32px;height:32px;border-radius:50%;background:var(--orange);color:var(--white);font-size:9px;font-weight:800;line-height:32px;text-align:center}

/* footer */
.footer-bg{left:0;top:2600px;width:1200px;height:316px}
.footer .brand{font-size:24px}
.fcol h4{color:var(--white);font-size:14px;font-weight:700;margin-bottom:18px}
.fcol li{list-style:none;color:#c7d5db;font-size:10.5px;line-height:22.6px}
.news p{color:#c7d5db;font-size:10.5px;margin-bottom:8px}
.news .field{width:162px;height:24px;border-radius:12px;background:var(--white);display:flex;align-items:center;justify-content:space-between;padding-left:10px;font-size:9.5px;color:#9aa3a9}
.news .go{width:24px;height:24px;border-radius:50%;background:var(--teal);display:flex;align-items:center;justify-content:center}
.social{display:flex;gap:6px;margin-top:14px}
.social span{width:16px;height:16px;border-radius:50%}
.copyright{left:0;top:2916px;width:1200px;height:30px;background:var(--teal-deep);color:var(--white);font-size:10px;text-align:center;line-height:30px;font-weight:600}
</style>
</head>
<body>

<!-- top bar -->
<div class="abs topbar">
  <span class="abs phone">&#9742; +1 555 0142 880</span>
  <span class="abs promo">FREE SHIPPING ON ORDERS OVER $40</span>
  <span class="abs account">&#9679; My Account</span>
  <span class="abs cart">&#9632; 3 Items</span>
</div>

<!-- navigation -->
<header class="abs nav">
  <a class="abs brand" href="#"><span class="dot"></span>Tailwell Co.</a>
  <nav class="abs menu">
    <span class="drop">Our Story</span>
    <span class="drop">Products</span>
    <span class="drop">Pet Lover</span>
    <span class="drop">Pet Parent</span>
    <span>Pet memorials</span>
    <span>FAQs</span>
    <span>Contact</span>
  </nav>
</header>

<!-- hero -->
<section class="hero">
  <div class="abs hero-bg" role="img" aria-label="Photo of a dog playing on a lawn, tinted teal"></div>
  <svg class="abs hero-wave" width="1200" height="120" viewBox="0 0 1200 120" aria-hidden="true">
    <path d="M0 60 C 300 130, 700 -10, 1200 70 L1200 120 L0 120 Z" fill="#ffffff"/>
  </svg>
  <h1 class="abs">All Natural Delicious CBD Oils &amp; Treats For Your Pets</h1>
  <p class="abs">Lorem ipsum dolor sit amet, eos ad vocent verear efficiendi, illum indoctum no nec. No eum probo possit.</p>
  <a class="abs btn dark b1" href="#">Learn Our Story</a>
  <a class="abs btn orange b2" href="#">View Our Products</a>
  <div class="abs bag bag1" role="img" aria-label="CBD Treats bag with a photo of a dog"></div>
  <div class="abs bag bag2" role="img" aria-label="CBD Treats bag with a photo of a dog holding a ball"></div>
  <div class="abs bag bag3" role="img" aria-label="CBD Treats bag with a photo of a dog"></div>
</section>

<a class="abs pill dogs" href="#">
  <span class="face" role="img" aria-label="Dog illustration"></span>
  <span><small>Shop for</small><strong>Dogs</strong></span>
</a>
<a class="abs pill cats" href="#">
  <span><small>Shop for</small><strong>Cats</strong></span>
  <span class="face" role="img" aria-label="Cat illustration"></span>
</a>

<!-- decorative area -->
<div class="abs deco-wash" role="img" aria-label="Faint teal paw print and heart decoration"></div>

<!-- mission -->
<section class="mission">
  <h2 class="abs h2 mission-title">Our Mission</h2>
  <p class="abs mission-lead">Lorem ipsum dolor sit amet, eos ad vocent verear efficiendi, illum indoctum no nec. No eum probo possit. Ut nam semper audire, ius tantas commodo viderer cu.</p>
  <div class="abs badges">
    <div class="badge">
      <div class="ring"><svg width="34" height="34" viewBox="0 0 34 34"><path d="M17 4 C21 12 21 20 17 28 C13 20 13 12 17 4Z M17 28 L17 32" fill="none" stroke="#33b8a4" stroke-width="2"/></svg></div>
      <span>Full Spectrum Cannabinoids</span>
    </div>
    <div class="badge">
      <div class="ring"><svg width="34" height="34" viewBox="0 0 34 34"><path d="M13 5 H21 M15 5 V14 L8 28 H26 L19 14 V5" fill="none" stroke="#33b8a4" stroke-width="2" stroke-linejoin="round"/></svg></div>
      <span>Lab Tested</span>
    </div>
    <div class="badge">
      <div class="ring"><svg width="40" height="40" viewBox="0 0 40 40"><text x="20" y="24" text-anchor="middle" font-family="Mulish,sans-serif" font-weight="800" font-size="11" fill="#33b8a4">GMO</text><line x1="8" y1="32" x2="32" y2="8" stroke="#33b8a4" stroke-width="2"/></svg></div>
      <span>Non GMO</span>
    </div>
    <div class="badge">
      <div class="ring"><svg width="38" height="38" viewBox="0 0 38 38"><g fill="none" stroke="#33b8a4" stroke-width="2"><circle cx="14" cy="24" r="4"/><circle cx="24" cy="14" r="4"/><line x1="7" y1="31" x2="31" y2="7"/></g></svg></div>
      <span>Soy Free</span>
    </div>
  </div>
  <div class="abs mission-body">
    <p>Our treats and oils start with whole hemp grown on small family farms that share our care for the land. Every batch is tested twice by an outside lab so you always know exactly what goes into the bowl, and nothing artificial is ever added to the recipe. We keep our list of ingredients short, clear and easy to read, so every pet parent can choose with total confidence.</p>
    <p>We believe pets deserve the same care we give ourselves. That is why we pair gentle, natural ingredients with honest labels, simple doses and friendly support from people who truly love animals as much as you do. Whether your companion is young and busy or older and slowing down, we are here to help them feel calm, comfortable and ready for every walk.</p>
    <p>Every order helps a local rescue shelter, because a happy, healthy life should be within reach of every pet, whether they nap on a couch or still wait for a home and finds the love it deserves.</p>
  </div>
  <a class="abs btn orange more" href="#">Learn more</a>
</section>

<!-- benefits -->
<section class="benefits">
  <h2 class="abs h2 benefits-title">Hemp oil extract benefits<br>for pets and people</h2>
  <div class="abs pets-photo" role="img" aria-label="Photo of a tabby cat sitting beside a golden retriever"></div>
  <div class="abs benefit" style="left:548px;top:1132px"><i></i>Cancer</div>
  <div class="abs benefit" style="left:548px;top:1189px"><i></i>Digestive &amp; Nausea</div>
  <div class="abs benefit" style="left:548px;top:1246px"><i></i>Anxiety &amp; Phobias</div>
  <div class="abs benefit" style="left:548px;top:1303px"><i></i>Joints &amp; Mobility</div>
  <div class="abs benefit" style="left:548px;top:1366px"><i></i>Pain &amp; Inflammation</div>
  <div class="abs benefit" style="left:758px;top:1132px"><i></i>Epilepsy &amp; Seizures</div>
  <div class="abs benefit" style="left:758px;top:1189px"><i></i>Aging &amp; Wellness</div>
  <div class="abs benefit" style="left:758px;top:1246px"><i></i>Heart &amp; Circulatory</div>
  <div class="abs benefit" style="left:758px;top:1303px"><i></i>Skin &amp; Allergies</div>
  <div class="abs benefit" style="left:758px;top:1366px"><i></i>Infectious Diseases</div>
</section>

<!-- testimonials -->
<section class="testimonials">
  <div class="abs testi-bg" role="img" aria-label="Photo of a dog running on grass, tinted teal"></div>
  <svg class="abs" style="left:0;top:1465px" width="1200" height="90" viewBox="0 0 1200 90" aria-hidden="true">
    <path d="M0 0 H1200 V40 C 900 100, 500 -20, 0 60 Z" fill="#ffffff"/>
  </svg>
  <svg class="abs" style="left:0;top:2010px" width="1200" height="60" viewBox="0 0 1200 60" aria-hidden="true">
    <path d="M0 60 V50 C 400 10, 800 70, 1200 40 V60 Z" fill="#ffffff"/>
  </svg>
  <h2 class="abs h2 testi-title">Testimonials</h2>

  <div class="abs arrow" style="left:201px;top:1808px"><svg width="10" height="10" viewBox="0 0 10 10"><path d="M7 1 L3 5 L7 9" fill="none" stroke="#33b8a4" stroke-width="1.6"/></svg></div>
  <div class="abs arrow" style="left:970px;top:1808px"><svg width="10" height="10" viewBox="0 0 10 10"><path d="M3 1 L7 5 L3 9" fill="none" stroke="#33b8a4" stroke-width="1.6"/></svg></div>

  <article class="abs card" style="left:251px;top:1701px">
    <div class="avatar" role="img" aria-label="Photo of Krypto the dog"></div>
    <h3>Krypto</h3>
    <div class="stars">★★★★★</div>
    <p class="issues"><b>Health Issues:</b> Anxiety, Pain</p>
    <p>Albucius partiendo vel in, ei minimum oportere disputationi mea. Eros zril salutatus ex sit. Ut omnium ad modum maiorum pro, vitae discere facimates ex pro, te meo doctus iuvaret... <span class="read">Read More</span></p>
  </article>
  <article class="abs card" style="left:490px;top:1701px">
    <div class="avatar" role="img" aria-label="Photo of Cupcake the cat" style="background:linear-gradient(160deg,#a9aaa8,#55585a)"></div>
    <h3>Cupcake</h3>
    <div class="stars">★★★★★</div>
    <p class="issues"><b>Health Issues:</b> Anxiety, Pain</p>
    <p>Albucius partiendo vel in, ei minimum oportere disputationi mea. Eros zril salutatus ex sit. Ut omnium ad modum maiorum pro, vitae discere facimates ex pro, te meo doctus iuvaret... <span class="read">Read More</span></p>
  </article>
  <article class="abs card" style="left:729px;top:1701px">
    <div class="avatar" role="img" aria-label="Photo of Ghost the dog" style="background:linear-gradient(160deg,#f2efec,#9a8e86)"></div>
    <h3>Ghost</h3>
    <div class="stars">★★★★★</div>
    <p class="issues"><b>Health Issues:</b> Anxiety, Pain</p>
    <p>Albucius partiendo vel in, ei minimum oportere disputationi mea. Eros zril salutatus ex sit. Ut omnium ad modum maiorum pro, vitae discere facimates ex pro, te meo doctus iuvaret... <span class="read">Read More</span></p>
  </article>

  <a class="abs btn orange testi-btn" href="#">View All Testimonials</a>
</section>

<!-- most popular -->
<section class="popular">
  <h2 class="abs h2 pop-title">Most Popular</h2>
  <div class="abs arrow grey" style="left:201px;top:2273px"><svg width="10" height="10" viewBox="0 0 10 10"><path d="M7 1 L3 5 L7 9" fill="none" stroke="#8a9399" stroke-width="1.6"/></svg></div>
  <div class="abs arrow grey" style="left:969px;top:2273px"><svg width="10" height="10" viewBox="0 0 10 10"><path d="M3 1 L7 5 L3 9" fill="none" stroke="#8a9399" stroke-width="1.6"/></svg></div>
  <div class="abs featured"></div>
  <div class="abs sale">Sale</div>

  <div class="abs product" style="left:248px;top:2200px">
    <div class="pbag bag" role="img" aria-label="CBD Treats bag with a photo of a puppy"></div>
    <div class="name">CBD Treats</div><div class="price">$149.99</div>
    <a class="btn outline" href="#">Add to cart</a>
  </div>
  <div class="abs product" style="left:428px;top:2200px">
    <div class="pbag bag" role="img" aria-label="CBD Treats bag with a photo of a puppy"></div>
    <div class="name">CBD Treats</div><div class="price">$149.99</div>
    <a class="btn orange" href="#">Add to cart</a>
  </div>
  <div class="abs product" style="left:610px;top:2200px">
    <div class="pbag bag" role="img" aria-label="CBD Treats bag with a photo of a puppy"></div>
    <div class="name">CBD Treats</div><div class="price">$149.99</div>
    <a class="btn outline" href="#">Add to cart</a>
  </div>
  <div class="abs product" style="left:790px;top:2200px">
    <div class="pbag bag" role="img" aria-label="CBD Treats bag with a photo of a puppy"></div>
    <div class="name">CBD Treats</div><div class="price">$149.99</div>
    <a class="btn outline" href="#">Add to cart</a>
  </div>
</section>

<!-- footer -->
<footer class="footer">
  <svg class="abs footer-bg" width="1200" height="316" viewBox="0 0 1200 316" aria-hidden="true">
    <path d="M0 20 C 350 70, 800 -20, 1200 30 V316 H0 Z" fill="#0d3142"/>
  </svg>
  <a class="abs brand" href="#" style="left:250px;top:2764px">Tailwell Co.</a>

  <div class="abs fcol" style="left:430px;top:2708px">
    <h4>Info</h4>
    <ul><li>Our Story</li><li>Products</li><li>Pet Lovers</li><li>Pet parents</li><li>Pet Memorials</li></ul>
  </div>
  <div class="abs fcol" style="left:550px;top:2708px">
    <h4>More Info</h4>
    <ul><li>FAQs</li><li>More about CBD</li><li>Testimonials</li><li>Specialty Items</li><li>Memorials</li></ul>
  </div>
  <div class="abs fcol" style="left:670px;top:2708px">
    <h4>Support</h4>
    <ul><li>Contact</li><li>My Account</li><li>Shipping &amp; Returns</li><li>Privacy Policy</li><li>Terms of Service</li></ul>
  </div>
  <div class="abs fcol news" style="left:790px;top:2708px">
    <h4>Newsletter</h4>
    <p>Get our latest updates</p>
    <div class="field">Your Email
      <span class="go"><svg width="10" height="10" viewBox="0 0 10 10"><path d="M1 5 L9 1 L6 9 L5 6 Z" fill="#ffffff"/></svg></span>
    </div>
    <div class="social">
      <span style="background:#3b5998"></span>
      <span style="background:#1da1f2"></span>
      <span style="background:#e1306c"></span>
    </div>
  </div>

  <div class="abs copyright">Copyright © 2019 Tailwell Co.</div>
</footer>

</body>
</html>
```